Veltrano - Mechanic/Collision Center Business Card

We're looking for a business card design for our mechanic/ collision repair shop.

Can be with colours or monochromatic.

See the attached files.

Many thanks

```html
<!DOCTYPE html>
<html lang="en">
<head>
<meta charset="UTF-8">
<title>Veltrano – Business Card</title>
<link href="https://fonts.googleapis.com/css2?family=Baloo+2:wght@700;800&family=Roboto:wght@400;500&display=swap" rel="stylesheet">
<style>
  :root {
    --bg: #c4dcee;
    --brand-blue: #5b9fd6;
    --ink: #1d1d1f;
    --paper: #ffffff;
  }
  * { margin: 0; padding: 0; box-sizing: border-box; }
  html, body { width: 789px; height: 1200px; overflow: hidden; }
  body {
    background: var(--bg);
    position: relative;
    font-family: "Roboto", Arial, sans-serif;
    color: var(--ink);
  }
  .card {
    position: absolute;
    top: 311px;
    width: 330px;
    height: 578px;
    box-shadow: 0 10px 28px rgba(40, 80, 120, 0.22);
    text-align: center;
  }
  .card--back { left: 39px; background: var(--brand-blue); color: var(--paper); }
  .card--front { left: 420px; background: var(--paper); }
  .abs { position: absolute; left: 0; right: 0; }

  .wordmark {
    font-family: "Baloo 2", "Arial Rounded MT Bold", sans-serif;
    font-weight: 800;
    font-size: 40px;
    letter-spacing: 1px;
    line-height: 1;
  }
  .card--back .wordmark { top: 290px; color: var(--paper); }
  .card--front .wordmark { top: 82px; color: var(--ink); }

  .social {
    top: 505px;
    display: flex;
    justify-content: center;
    align-items: center;
    gap: 7px;
    font-family: "Baloo 2", sans-serif;
    font-weight: 700;
    font-size: 21px;
    line-height: 1;
  }
  .social__dot { width: 20px; height: 20px; border-radius: 50%; background: var(--paper); }
  .rule { position: absolute; left: 50%; height: 2px; transform: translateX(-50%); }
  .card--back .rule { top: 542px; width: 84px; background: var(--paper); }

  .company {
    top: 198px;
    font-family: "Baloo 2", sans-serif;
    font-weight: 800;
    font-size: 21px;
    line-height: 1;
  }
  .company__name { color: var(--brand-blue); }
  .card--front .rule { background: var(--brand-blue); width: 84px; }
  .rule--title { top: 234px; }
  .rule--contact { top: 402px; }

  .icons { top: 279px; display: flex; justify-content: center; gap: 21px; }
  .icon { width: 28px; height: 28px; }

  .contact { top: 326px; font-size: 14px; line-height: 22.5px; }
  .label { color: var(--brand-blue); font-weight: 500; font-size: 14px; line-height: 1; }
  .value { font-size: 14px; line-height: 1; }
  .label--postal { top: 449px; }
  .value--postal { top: 472px; }
  .label--person { top: 505px; }
  .value--person { top: 528px; }
</style>
</head>
<body>
  <section class="card card--back">
    <div class="abs wordmark">VELTRANO</div>
    <div class="abs social"><span class="social__dot"></span><span>/veltrano</span></div>
    <div class="rule"></div>
  </section>

  <section class="card card--front">
    <div class="abs wordmark">VELTRANO</div>
    <div class="abs company"><span class="company__name">Veltrano,</span> LDA</div>
    <div class="rule rule--title"></div>

    <div class="abs icons">
      <svg class="icon" viewBox="0 0 28 28" aria-label="Email">
        <circle cx="14" cy="14" r="14" fill="#5b9fd6"/>
        <rect x="7.5" y="9.5" width="13" height="9" rx="1.5" fill="#fff"/>
        <path d="M7.8 10.2 L14 15 L20.2 10.2" fill="none" stroke="#5b9fd6" stroke-width="1.3"/>
      </svg>
      <svg class="icon" viewBox="0 0 28 28" aria-label="Phone">
        <circle cx="14" cy="14" r="14" fill="#5b9fd6"/>
        <path d="M10 8 L12.3 8 L13.3 11.3 L11.8 12.5 C12.6 14.3 13.7 15.4 15.5 16.2 L16.7 14.7 L20 15.7 L20 18 C20 19 19.2 19.8 18.2 19.7 C12.9 19.2 8.8 15.1 8.3 9.8 C8.2 8.8 9 8 10 8 Z" fill="#fff"/>
      </svg>
      <svg class="icon" viewBox="0 0 28 28" aria-label="Location">
        <circle cx="14" cy="14" r="14" fill="#5b9fd6"/>
        <path d="M14 7.5 C11.2 7.5 9.3 9.5 9.3 12 C9.3 15.2 14 20 14 20 C14 20 18.7 15.2 18.7 12 C18.7 9.5 16.8 7.5 14 7.5 Z" fill="#fff"/>
        <circle cx="14" cy="12" r="1.8" fill="#5b9fd6"/>
      </svg>
    </div>

    <div class="abs contact">
      veltrano.mail@corvomail.com<br>
      +351 213407852 (or just 213407852)<br>
      Rua das Oficinas, 42
    </div>
    <div class="rule rule--contact"></div>

    <div class="abs label label--postal">Postal code</div>
    <div class="abs value value--postal">1900-318 Lisboa</div>
    <div class="abs label label--person">Rui Marques</div>
    <div class="abs value value--person">+351 912740586 (or just 912740586)</div>
  </section>
</body>
</html>
```